Looking to design a new sign for our church.

Looking for a new sign
4 x 8 feet dimension
We are renaming the church "Keller Ridge Community Church"
looking for legible graphics
Would like some type of backdrop being a family tree (oak) / open to other ideas as you are led
I have included a pic of the old sign for your review
would like to incorporate our Harvest Fields Mission on the lower right hand corner of the sign / see file attached

```html
<!DOCTYPE html>
<html lang="en">
<head>
<meta charset="utf-8">
<title>Keller Ridge Community Church – Sign</title>
<link rel="stylesheet" href="https://fonts.googleapis.com/css2?family=Abril+Fatface&family=Playfair+Display:ital,wght@1,900&family=Montserrat:wght@500&display=swap">
<style>
  :root {
    --page: #f2f2f2;
    --sign: #f3f0e6;
    --ink: #0d0d0d;
    --row-fill: #efefef;
    --tree-soft: #d9d5c8;
  }
  * { box-sizing: border-box; margin: 0; padding: 0; }
  html, body { width: 1200px; height: 838px; overflow: hidden; background: var(--page); }
  .sign {
    position: absolute; left: 60px; top: 92px;
    width: 1080px; height: 654px;
    background: var(--sign);
    overflow: hidden;
    box-shadow: 0 0 0 22px #fff;
  }
  .tree-outline {
    position: absolute; left: 0; top: 60px; width: 165px; height: 292px;
    background: radial-gradient(ellipse at 55% 45%, var(--tree-soft), rgba(243,240,230,0) 70%);
  }
  .tree-silhouette {
    position: absolute; left: 787px; top: 264px; width: 293px; height: 390px;
    background: radial-gradient(ellipse at 55% 40%, #1a1a1a 0%, #2a2a2a 45%, rgba(243,240,230,0) 72%);
  }
  .ministry {
    position: absolute; left: 640px; top: 540px; width: 140px; height: 100px;
    display: flex; flex-direction: column; align-items: center; justify-content: flex-end; gap: 8px;
  }
  .ministry-dot { width: 40px; height: 40px; border-radius: 50%; background: var(--ink); }
  .ministry-name {
    font-family: "Montserrat", sans-serif; font-weight: 500; font-size: 15px;
    color: var(--ink); text-align: center; line-height: 1.25;
  }
  .church-name {
    position: absolute; left: 338px; top: 48px;
    font-family: "Abril Fatface", serif; font-weight: 400; font-size: 132px; line-height: 121px;
    color: var(--ink); letter-spacing: -1px;
  }
  .name-rule {
    position: absolute; left: 340px; top: 318px; width: 292px; height: 2px; background: var(--ink);
  }
  .church-kind {
    position: absolute; left: 338px; top: 332px;
    font-family: "Playfair Display", serif; font-style: italic; font-weight: 900;
    font-size: 36px; letter-spacing: 3px; color: var(--ink); white-space: nowrap;
  }
  .schedule { position: absolute; left: 60px; top: 424px; list-style: none; }
  .schedule li {
    display: flex; width: 539px; height: 40px; margin-bottom: 22px;
    border: 1.5px solid var(--ink); background: var(--row-fill);
    font-family: "Montserrat", sans-serif; font-weight: 500; font-size: 33px; line-height: 37px;
    white-space: nowrap;
  }
  .schedule .time { width: 154px; background: var(--ink); color: #fff; padding-left: 4px; }
  .schedule .event { padding-left: 17px; color: var(--ink); }
</style>
</head>
<body>
  <div class="sign">
    <div class="tree-outline" role="img" aria-label="Outline line drawing of a leafy tree branch"></div>
    <h1 class="church-name">Keller<br>Ridge</h1>
    <div class="name-rule"></div>
    <p class="church-kind">Community Church</p>
    <ul class="schedule">
      <li><span class="time">10:30am</span><span class="event">Worship Service</span></li>
      <li><span class="time">9:30am</span><span class="event">Sunday School</span></li>
      <li><span class="time">6:00pm</span><span class="event">Wednesday Service</span></li>
    </ul>
    <div class="tree-silhouette" role="img" aria-label="Black silhouette of a spreading oak tree with leaves"></div>
    <div class="ministry">
      <span class="ministry-dot"></span>
      <span class="ministry-name">Harvest Fields Mission</span>
    </div>
  </div>
</body>
</html>
```